Banner Ad

We need a banner ad for a service. The service is called, "BrightNote" It compiles tweets and Friendwall posts about state government issues that are posted by U.S. State Legislators. We have a word cloud containing the issues we want to highlight. And we a logo for BrightNote.

The tag is:
Question: Who Is Talking About Issues on Social Media?
Answer: State Legislators
Are you Listening?

The banner ad will be used for print and web. It will go into a regular weekly publication called Monday Capitol Digest. http://www.civicmarlow.example/monday-capitol-digest/

Industry/Entity Type

Government

```html
<!DOCTYPE html>
<html lang="en">
<head>
<meta charset="utf-8">
<title>BrightNote Banner</title>
<link href="https://fonts.googleapis.com/css2?family=Marcellus+SC&family=Roboto+Condensed:wght@400;700&display=swap" rel="stylesheet">
<style>
  :root {
    --teal-deep: #1f5f6c;
    --teal-mid: #3f97a8;
    --cyan-light: #a9e3f0;
    --mint: #9fe0b0;
    --ink: #10283a;
    --ink-soft: #1a3848;
    --cloud-light: #f3fbff;
    --navy: #1d2d5a;
    --band: rgba(235, 250, 252, 0.55);
    --icon: #8e9a9c;
    --ring: rgba(255, 255, 255, 0.55);
  }
  * { margin: 0; padding: 0; box-sizing: border-box; }
  html, body { width: 1200px; height: 927px; overflow: hidden; }
  .banner {
    position: relative;
    width: 1200px;
    height: 927px;
    overflow: hidden;
    background:
      radial-gradient(ellipse 520px 420px at 330px 470px, rgba(200,240,250,0.85), transparent 70%),
      radial-gradient(ellipse 520px 260px at 820px 900px, var(--mint), transparent 75%),
      linear-gradient(160deg, var(--teal-deep) 0%, var(--teal-mid) 35%, var(--cyan-light) 60%, #7ec9d6 85%, #6fb7a8 100%);
    font-family: "Roboto Condensed", "Arial Narrow", sans-serif;
  }
  .tagline {
    position: absolute;
    top: 78px;
    left: 0;
    width: 1180px;
    text-align: center;
    font-family: "Marcellus SC", serif;
    color: #ffffff;
    font-size: 27px;
    line-height: 39px;
    letter-spacing: 2.5px;
    word-spacing: 8px;
  }
  .map-area {
    position: absolute;
    left: 0;
    top: 210px;
    width: 620px;
    height: 450px;
    border-radius: 40% 30% 35% 30%;
    background: linear-gradient(135deg, #0f5b7a 0%, #1c8fa6 45%, #39c4c8 80%, #2a8aa8 100%);
    opacity: 0.85;
  }
  .ring {
    position: absolute;
    left: 0;
    top: 0;
  }
  .word {
    position: absolute;
    line-height: 1;
    white-space: nowrap;
    transform: scaleX(0.75);
  }
  .left { right: 288px; text-align: right; transform-origin: right center; }
  .right { left: 925px; transform-origin: left center; }
  .light { color: var(--cloud-light); }
  .dark { color: var(--ink); }
  .brand-band {
    position: absolute;
    left: 0;
    top: 738px;
    width: 1183px;
    height: 120px;
    background: var(--band);
  }
  .brand-name {
    position: absolute;
    left: 180px;
    top: 772px;
    font-family: "Marcellus SC", serif;
    font-size: 54px;
    color: var(--navy);
    letter-spacing: 1px;
  }
  .social {
    position: absolute;
    right: 20px;
    display: flex;
    align-items: center;
    gap: 8px;
    font-family: "Marcellus SC", serif;
    font-size: 31px;
    color: var(--ink-soft);
  }
  .social-dot {
    width: 36px;
    height: 36px;
    border-radius: 50%;
    background: var(--icon);
  }
  .social-wall { top: 755px; }
  .social-chirp { top: 809px; }
</style>
</head>
<body>
<div class="banner">
  <p class="tagline">
    Question: Who Is Talking About Issues on Social Media?<br>
    Answer: State Legislators!<br>
    Question: Are you Listening?
  </p>

  <div class="map-area" role="img" aria-label="Map of the United States with each state shaded in teal and blue tones"></div>
  <svg class="ring" width="1200" height="927" aria-hidden="true">
    <circle cx="322" cy="455" r="226" fill="none" stroke="var(--ring)" stroke-width="5"/>
  </svg>

  <div class="word-cloud">
    <span class="word left light" style="top:258px;font-size:68px;">MinimumWage</span>
    <span class="word left dark" style="top:334px;font-size:30px;">AlternativeEnergy</span>
    <span class="word left light" style="top:375px;font-size:26px;">Drones</span>
    <span class="word left dark" style="top:417px;font-size:40px;">SharingEconomy</span>
    <span class="word left light" style="top:480px;font-size:20px;opacity:.9;">FairShare</span>
    <span class="word left dark" style="top:500px;font-size:72px;">Transportation</span>
    <span class="word left light" style="top:573px;font-size:44px;">Immigration</span>
    <span class="word left dark" style="top:627px;font-size:27px;">DistractedDriving</span>

    <span class="word right light" style="top:268px;font-size:44px;">GMO</span>
    <span class="word right dark" style="top:310px;font-size:60px;">CommonCore</span>
    <span class="word right light" style="top:375px;font-size:56px;">Fracking</span>
    <span class="word right dark" style="top:437px;font-size:23px;">Privacy</span>
    <span class="word right light" style="top:477px;font-size:24px;">Bankruptcy</span>
    <span class="word right dark" style="top:518px;font-size:36px;">E-Cigs</span>
    <span class="word right light" style="top:563px;font-size:29px;">TaxReform</span>
    <span class="word right dark" style="top:600px;font-size:56px;">ClimateChange</span>
  </div>

  <div class="brand-band"></div>
  <div class="brand-name">BrightNote</div>
  <div class="social social-wall"><span class="social-dot"></span><span>/CivicMarlowAssociates</span></div>
  <div class="social social-chirp"><span class="social-dot"></span><span>@CivicMarlowAssoc</span></div>
</div>
</body>
</html>
```